Homepage for the lumo-pathe Web Application

At the end of this text, you will find a link to a website that is under construction for a webApp that I intend to launch soon. The contest goal is for you to make redesign the homepage in a nice, fresh, modern Style. Only design, no coding necessary. It needs to have a responsive version for small screens like smart phones. Attached is the text for it, and some images that you may use. You are welcome to find or create additional supporting images. You can use PixaVendor.example or similar service to find new images as long as I can purchase the non-exclusive use rights for the images at similar prices. The contest is just for the home page. However, the winner, if I like the work and we can agree on a fair price, could be contracted on a one-on-one basis to do the rest of the site. You are welcome to suggest minor changes like font sizes and minor variations on the Header banner, but that banner is consistent with the user interface of the application therefore should not change too much. The information should flow somewhat continually without much use of side bars or things like that.
https://www.lumo-pathe.example
Sincerely,
Marek D. Holloway

```html
<!DOCTYPE html>
<html lang="en">
<head>
<meta charset="utf-8">
<title>Lumo-Pathe — Find any document or item instantly</title>
<link href="https://fonts.googleapis.com/css2?family=Poppins:wght@400;500;600;700&display=swap" rel="stylesheet">
<style>
:root{
  --mat:#58d6d8;
  --header:#3f86d0;
  --nav:#0b6eb3;
  --field:#5fa4ea;
  --ink:#333a44;
  --muted:#6f7680;
  --orange:#f26b3f;
  --grey-bg:#f4f5f7;
  --navy:#173a72;
  --teal:#3cc3cc;
  --teal-soft:#d7f3f5;
  --white:#ffffff;
}
*{box-sizing:border-box;margin:0;padding:0}
html,body{width:1200px;height:4332px;overflow:hidden}
body{background:var(--mat);font-family:"Poppins",sans-serif;color:var(--ink)}
.page{position:absolute;left:87px;top:87px;width:1024px;height:4155px;background:var(--white);overflow:hidden}
.abs{position:absolute}

/* header */
.topbar{position:absolute;left:0;top:0;width:100%;height:64px;background:var(--header)}
.brand{display:flex;align-items:center;gap:6px;font-size:21px;font-weight:500;color:var(--white);white-space:nowrap}
.brand-dot{width:20px;height:20px;border-radius:50%;background:var(--white);flex:none}
.topbar .brand{position:absolute;left:58px;top:18px}
.field{position:absolute;top:15px;height:34px;border-radius:6px;background:var(--field);color:#eaf4ff;font-size:12px;padding:9px 10px}
.field.user{left:221px;width:280px}
.field.pass{left:524px;width:280px;color:#2a7fd6}
.login{position:absolute;left:828px;top:14px;width:128px;height:36px;border:2px solid var(--white);border-radius:6px;color:var(--white);font-size:14px;text-align:center;line-height:32px}
.navbar{position:absolute;left:0;top:64px;width:100%;height:34px;background:var(--nav);display:flex;justify-content:center;align-items:center;gap:18px;font-size:13px;color:var(--white)}

/* hero */
.hero-title{left:69px;top:178px;font-size:39px;font-weight:700;line-height:46px;color:var(--ink)}
.hero-text{left:69px;top:305px;width:420px;font-size:13px;line-height:22px;color:var(--muted)}
.btn{display:block;background:var(--orange);color:var(--white);font-size:15px;font-weight:500;text-align:center;border-radius:8px;box-shadow:0 6px 14px rgba(242,107,63,.35)}
.hero-btn{left:69px;top:395px;width:227px;height:56px;line-height:56px}
.art{border-radius:18px;background:linear-gradient(145deg,var(--teal-soft),var(--teal) 70%,#e77552)}

/* intro */
.sub-title{font-size:22px;font-weight:600;line-height:37px;color:var(--ink)}
.body-text{font-size:13.5px;line-height:23px;color:var(--muted)}

/* grey section */
.grey{left:0;top:997px;width:100%;height:1966px;background:var(--grey-bg)}
.why-title{left:0;top:1050px;width:100%;text-align:center;font-size:22px;font-weight:500;line-height:37px}
.rule{left:467px;top:1122px;width:92px;height:3px;background:var(--orange)}
.h3{font-size:19px;font-weight:500;color:var(--ink)}
.h3::before{content:"›";color:var(--orange);font-weight:700;margin-right:10px}
.para-block p{margin-bottom:23px}
.cards{left:69px;top:1770px;width:888px;display:flex;flex-direction:column;gap:17px}
.card{background:var(--white);border-radius:8px;padding:20px 20px 22px}
.card.active{border-bottom:5px solid var(--orange)}
.card h4{font-size:15px;font-weight:500;margin-bottom:12px;color:var(--ink)}
.card h4::before{content:"•";color:var(--orange);margin-right:6px}
.card p{font-size:12px;line-height:20px;color:var(--muted)}

/* cta */
.cta{left:0;top:3333px;width:100%;height:249px;background:var(--navy);text-align:center;color:var(--white)}
.cta h2{margin-top:53px;font-size:22px;font-weight:600}
.cta p{margin-top:10px;font-size:13.5px}
.cta .btn{width:226px;height:56px;line-height:56px;margin:28px auto 0}

/* why list */
.why-list{list-style:none;font-size:14px;line-height:23px;color:var(--muted)}
.why-list li::before{content:"•";color:var(--orange);margin-right:5px}
.why-list a{color:var(--orange)}

/* footer */
.footer{left:0;top:4005px;width:100%;height:150px;border-top:1px solid #eceef1}
.footer .brand{position:absolute;left:95px;top:38px;color:#3a4a6b;font-size:24px}
.footer .brand-dot{background:var(--teal)}
.foot-nav{position:absolute;left:296px;top:36px;font-size:12px;color:var(--muted)}
.foot-nav b{display:block;font-weight:600;color:var(--ink);margin-bottom:8px}
.copy{position:absolute;left:0;top:118px;width:100%;text-align:center;font-size:10px;color:var(--muted)}
</style>
</head>
<body>
<div class="page">
  <header class="topbar">
    <div class="brand"><span class="brand-dot"></span>Lumo Pathe</div>
    <div class="field user">sample.user42</div>
    <div class="field pass">password</div>
    <div class="login">Login</div>
  </header>
  <nav class="navbar"><span>About</span><span>Pricing</span><span>Blog</span><span>Reviews</span><span>Support</span><span>FAQs</span><span>Contact Us</span></nav>

  <h1 class="abs hero-title">Find any document<br>or item instantly!</h1>
  <p class="abs hero-text">Lumo-Pathe helps you save considerable space without losing speedy accessibility to your treasured items.</p>
  <a class="abs btn hero-btn">Get 30 Days Free Trial</a>
  <div class="abs art" style="left:540px;top:148px;width:402px;height:345px" role="img" aria-label="Isometric illustration of a businessman in an open laptop drawer holding an orange folder"></div>

  <div class="abs art" style="left:64px;top:619px;width:219px;height:328px" role="img" aria-label="Illustration of a phone showing filing drawers and folders"></div>
  <h2 class="abs sub-title" style="left:373px;top:650px;width:580px">Keeping track of all your paper documents and other belongings has never been easier!</h2>
  <p class="abs body-text" style="left:373px;top:738px;width:560px">Lumo-Pathe is a system that allows you to quickly search for the location of every item that you store or file. It is an essential tool for keeping track of paper documents or any other kind of physical item. You'll have the ability to quickly find any item you're searching for, even years after you've stored it. More importantly, using Lumo-Pathe helps you save considerable space without losing speedy accessibility to your treasured items.</p>

  <div class="abs grey"></div>
  <h2 class="abs why-title">Why use a storage management system<br>like Lumo-Pathe?</h2>
  <div class="abs rule"></div>

  <h3 class="abs h3" style="left:69px;top:1160px">Managing paper documents</h3>
  <div class="abs body-text para-block" style="left:69px;top:1207px;width:508px">
    <p>Most people and businesses have a variety of documents that need to be filed. The problem is how to do it efficiently so that anything you need can easily be found, even well into the future. Normally, you'd put them in folders on file drawers, sorted in some sort of fashion. But which standard is correct for all kinds of documents? There is no set criterion for every kind of document, so you need to use a combination of them.</p>
    <p>As time passes, you might have a difficult time recalling what criterion you used to file your documents, making it hard to find that document with ease. You might not even find it at all. It becomes even more complex when the person doing the searching isn't the same one as who filed it years ago.</p>
    <p>It is estimated that workers spend over 20% of their time managing documents. A storage management system like Lumo-Pathe allows any authorized user to instantly find any document regardless of who filed it or which criterion was used, as long as it was properly filed using the system.</p>
  </div>
  <div class="abs art" style="left:619px;top:1215px;width:328px;height:396px" role="img" aria-label="Illustration of a businessman carrying an orange binder into a phone-shaped filing cabinet"></div>

  <h3 class="abs h3" style="left:69px;top:1682px">Managing any non-document objects</h3>
  <p class="abs body-text" style="left:69px;top:1720px;font-size:13px">The same is true of storing any other kind of objects. Common examples include:</p>

  <div class="abs cards">
    <div class="card active"><h4>Storage boxes, closets, warehouses, and shelves</h4><p>Anything that you put away in storage, would better be indexed with a system that lets you find what you're looking for instantly. Otherwise, you are better off getting rid of those items. In addition to helping you find any object quickly and easily, proper use of Lumo-Pathe could help you save lots of space!</p></div>
    <div class="card"><h4>Books</h4><p>Whether you keep your books on display on shelves, or stored in boxes, you should keep them indexed if you ever want to find any of them in the future.</p></div>
    <div class="card"><h4>Wines</h4><p>Maintaining a constant temperature is essential for good care of quality wines. If you are a wine enthusiast, and have even a small wine cellar fridge, keeping your wines indexed on our system would prove invaluable in selecting and locating a wine bottle for any moment without opening that cellar fridge door for too long.</p></div>
    <div class="card"><h4>Safety Boxes</h4><p>It is common for people to forget exactly which valuables they have stored in their safety boxes or bank safety deposit boxes.</p></div>
    <div class="card"><h4>Movie Boxes</h4><p>It is always a good idea to record in detail the contents of each box when you move. Since Lumo-Pathe works well on any modern smartphone, it is easy to record each item as you pack it. After the move, the system makes it easy for you to check that everything that you packed arrived as it should. In addition, if you leave some boxes unopened for a long time, you will always be able to locate the items inside in no time.</p></div>
    <div class="card"><h4>Test Samples</h4><p>Laboratory samples frequently need to be stored at constant cold temperatures. Our system was originally designed to fulfill the needs of a laboratory which needs an efficient way to minimize the time that the door of their specialized freezers is open while searching for a sample. For confidentiality reasons, each vial was only identified with a code and all the details of the sample and patient would be recorded on our secure system.</p></div>
    <div class="card"><h4>Audio, video, data, and removable media</h4><p>Keeping track of the content and storage location of removable media can be a hassle. A system like ours can really help to make that task a breeze.</p></div>
    <div class="card"><h4>Keys</h4><p>In a situation such a property management, you can keep track of hundreds of keys for every property you manage. Using Lumo-Pathe will easily organize your key boxes without losing track of where the keys for each property are located.</p></div>
  </div>

  <div class="abs art" style="left:89px;top:3005px;width:236px;height:286px" role="img" aria-label="Illustration of a businessman holding a disc beside a phone-shaped cabinet"></div>
  <h2 class="abs sub-title" style="left:373px;top:3058px">Alternative uses for Lumo-Pathe</h2>
  <p class="abs body-text" style="left:373px;top:3101px;width:570px">How many times have you gone to a restaurant and couldn't recall how good (or bad) each of the dishes were that you previously ordered? You can use Lumo-Pathe to record each one to improve your experience for every visit. Our app can also help you decide where you want to go or which dish to recommend when you have a special occasion.</p>

  <section class="abs cta">
    <h2>Get Lumo-Pathe for Free</h2>
    <p>Keeping track of all your paper documents and other belongings has never been easier!</p>
    <a class="btn">Get 30 Days Free Trial</a>
  </section>

  <h2 class="abs sub-title" style="left:69px;top:3690px">Why Lumo-Pathe?</h2>
  <ul class="abs why-list" style="left:69px;top:3739px;width:600px">
    <li>It is extremely easy to use.</li>
    <li>It Adapts to your stile. Since each catalog can have 1 or more levels of depth (folders and sub-folders), Lumo-Pathe does not force you to use a specific filing or storage methodology.</li>
    <li>It's very affordable. <a>Checkout our pricing plans!</a></li>
    <li>Since it is online, your data is available almost anywhere in the world.</li>
    <li>Data encryption ensures that your information is always private, safe, and secure.</li>
  </ul>
  <div class="abs art" style="left:703px;top:3644px;width:227px;height:294px" role="img" aria-label="Illustration of a businessman holding a large orange key beside a phone-shaped cabinet"></div>

  <footer class="abs footer">
    <div class="brand"><span class="brand-dot"></span>Lumo Pathe</div>
    <div class="foot-nav"><b>Navigate</b>About &nbsp;|&nbsp; Pricing &nbsp;|&nbsp; Blog &nbsp;|&nbsp; Reviews &nbsp;|&nbsp; Support &nbsp;|&nbsp; FAQs &nbsp;|&nbsp; Contact Us</div>
    <p class="copy">Copyright © 2021 Brightfold Works LLC</p>
  </footer>
</div>
</body>
</html>
```